依頼概要
■依頼の目的/概要
インフルエンザワクチンのポスターを作成して頂きたいです。
クリニック内の待合室に掲示します。

■依頼詳細
A2サイズです。
温かみのある柔らかいデザインをお願いします。
ポスターには、人のイラスト入りでお願いします。イラストはご自身で書いてくださってもいいですし、フリー素材でも構いません。
色合いは当院ホームページを参考にしてください。
当院ホームページ https://temuzeku.com/

記載する内容については、添付ファイルを参照してください。
ロゴデータは当選決定後に送らせて頂きます。

納品は、元データ(aiファイルやpsdファイル)とPNG書き出しでお願いします。

■重視する点
過去・現在までにデザインの経験のある方を希望致します。

その他何かご不明な点がございましたら、お気軽にご質問下さい。
よろしくお願いいたします。

文字が大きく読みやすい、温かみのあるデザインです。

皆さま、この度は当コンペにご参加いただき、誠にありがとうございます。
どれも力作で魅力的で選ぶのが大変でした。
今後ともどうぞよろしくお願いします。

```html
<!DOCTYPE html>
<html lang="ja">
<head>
<meta charset="utf-8">
<title>インフルエンザ予防接種 ポスター</title>
<link rel="stylesheet" href="https://fonts.googleapis.com/css2?family=Noto+Sans+JP:wght@400;500;700;900&family=Shippori+Mincho+B1:wght@800&display=swap">
<style>
:root{
  --green:#5ea832;
  --green-dark:#3f8a20;
  --green-pale:#eaf3dc;
  --green-band:#d6e9bf;
  --orange:#e38a1c;
  --yellow:#f2c21b;
  --ink:#3b3b3b;
  --white:#ffffff;
}
*{margin:0;padding:0;box-sizing:border-box}
html,body{width:849px;height:1200px;overflow:hidden;background:var(--white)}
body{font-family:"Noto Sans JP",sans-serif;color:var(--ink)}
.poster{position:relative;width:849px;height:1200px;background:var(--white);overflow:hidden}

.badge{position:absolute;left:560px;top:24px;width:262px;height:110px;border:3px solid var(--green);border-radius:26px;background:var(--green-pale);
  display:flex;flex-direction:column;align-items:center;justify-content:center;color:var(--green-dark);font-weight:900;font-size:30px;line-height:1.25;z-index:2}
.badge-tail{position:absolute;left:590px;top:131px;z-index:2}

.date{position:absolute;left:62px;top:92px;font-weight:700;font-size:168px;line-height:1;color:var(--green);letter-spacing:-6px;white-space:nowrap}
.weekday{position:absolute;left:522px;top:186px;width:54px;height:54px;border-radius:50%;background:var(--yellow);color:var(--white);
  font-weight:900;font-size:30px;display:flex;align-items:center;justify-content:center}
.starts{position:absolute;left:520px;top:246px;font-weight:900;font-size:40px;line-height:1.2;color:var(--green);letter-spacing:1px;white-space:nowrap}

.no-booking{position:absolute;left:70px;top:312px;font-family:"Shippori Mincho B1",serif;font-weight:800;font-size:80px;line-height:1.25;color:var(--orange);white-space:nowrap;z-index:1}

.illustration{position:absolute;left:505px;top:305px;width:330px;height:505px;border-radius:40px;
  background:radial-gradient(ellipse at 50% 55%,#f6e9d6 0%,#eef4e4 60%,#ffffff 100%)}

.notes{position:absolute;left:72px;top:540px;width:425px;list-style:none;font-size:14.5px;line-height:1.55;font-weight:500;z-index:1}
.notes li{position:relative;padding-left:22px;margin-bottom:7px}
.notes li::before{content:"";position:absolute;left:0;top:6px;width:12px;height:12px;background:var(--green)}
.notes em{font-style:normal;color:var(--orange);font-weight:700}

.fees{position:absolute;left:0;top:848px;width:849px;height:272px;background:var(--green-band);padding:14px 60px}
.fee-grid{display:grid;grid-template-columns:250px 1fr;grid-template-rows:84px 92px 54px;gap:8px}
.age{background:var(--white);border-left:8px solid var(--green);padding:8px 14px;font-weight:900;color:var(--ink);display:flex;flex-direction:column;justify-content:center}
.age big{font-size:34px;color:var(--green-dark)}
.age .lg{font-size:26px}
.age small{font-size:13px;font-weight:500;line-height:1.35}
.age .tiny{font-size:10px;color:#777}
.price{background:var(--white);padding:12px 22px;font-weight:700}
.price.public{grid-row:span 2}
.price h3{font-size:24px;font-weight:700;color:var(--ink);margin-bottom:10px;border-bottom:1px solid #cfcfcf;padding-bottom:6px}
.price p{font-size:20px;line-height:1.5}
.price .yen{font-size:32px;color:var(--orange);font-weight:900}
.price .fine{font-size:11px;color:#777;font-weight:400;margin-top:6px}
.price.general{display:flex;align-items:center;font-size:20px}

.footer{position:absolute;left:0;top:1124px;width:849px;height:76px;display:flex;flex-direction:column;align-items:center;justify-content:center;gap:4px}
.footer small{font-size:10px;color:#777}
.clinic{display:flex;align-items:center;gap:8px;font-weight:700;font-size:24px;color:var(--green-dark)}
.clinic i{width:20px;height:20px;border-radius:50%;background:var(--green)}
</style>
</head>
<body>
<main class="poster">
  <div class="badge"><span>インフルエンザ</span><span>予防接種</span></div>
  <svg class="badge-tail" width="40" height="30" viewBox="0 0 40 30"><path d="M4 0 L16 26 L30 0" fill="#eaf3dc" stroke="#5ea832" stroke-width="3"/><rect x="4" y="0" width="28" height="3" fill="#eaf3dc"/></svg>

  <div class="date">10/11</div>
  <div class="weekday">金</div>
  <div class="starts">から始まります</div>

  <div class="illustration" role="img" aria-label="看護師が女性の腕に予防接種をしているやわらかなイラスト"></div>

  <h1 class="no-booking">予約は必要<br>ありません</h1>

  <ul class="notes">
    <li>インフルエンザに対する抵抗力がつくまで約2週間かかり、その効果は<em>約5ヶ月間持続</em>します。</li>
    <li>2回接種をご希望の方は、1回目接種から4週間後に2回目接種を行います。</li>
    <li>肺炎球菌ワクチンとの同時接種もできます。</li>
    <li>体温が37.5度以上、具合が悪い方は別の日に接種しましょう。</li>
    <li>当院では妊娠中の方も予防接種できます。</li>
  </ul>

  <section class="fees">
    <div class="fee-grid">
      <div class="age"><span><big>65歳</big>以上</span></div>
      <div class="price public">
        <h3>相模原市公費負担がございます</h3>
        <p>接種費用：<span class="yen">1,500円</span>（摂取回数1回）</p>
        <p>期間：10/11(金)～12/31(火)</p>
        <p class="fine">※期間や条件についてはお住まいの市にご確認ください。</p>
      </div>
      <div class="age"><span><span class="lg">60歳</span>以上<span class="lg">65歳</span>未満</span>
        <small>心臓・腎臓・肺に障害のある方*<br>HIV感染による免疫不全</small>
        <span class="tiny">※詳しくは受付にお問い合わせ下さい</span></div>
      <div class="age"><span><span class="lg">13歳</span>以上<span class="lg">65歳</span>未満</span></div>
      <div class="price general">接種費用：<span class="yen">4,000円</span>（2回目3,000円）</div>
    </div>
  </section>

  <footer class="footer">
    <small>内科・呼吸器内科・循環器内科・消化器内科</small>
    <div class="clinic"><i></i>みどり内科クリニック</div>
  </footer>
</main>
</body>
</html>
```